Thistlewood Group Business Card Design

We are looking for a new business card design, we are not happy with our current design. We are a boutique management consulting firm and our clients are typically meridian 400 companies.

I have attached the current front and back that we have as well as a version of our logo that can be used. I am trying to get a higher resolution version of the logo file to upload to the project.

Target Market(s)

Meridian 400 companies are our primary client base. Financial services, life sciences, pharmaceuticals and telecom companies are

Industry/Entity Type

Management Consulting

Contact Information for Business Card

We are trying to communicate a high degree of professionalism, a somewhat minimalist perhaps with some air of whimsy (without overdoing it). Attached is the current design, front and back as well as logos. I like the current back of the card and assume we will keep the phrase the same.

From a color palette perspective, I prefer to stay with a gray scale as they are today.

Font styles to use
Sans Serif

Colors
1b1b1b
474747
ffffff

Requirements
Must have
• Two sided business card design. File format should be something that can be used outside of Photoshop like MS Publisher so that they can be edited with personal information.
• Font should be calibri or something very similar and should be available within MS Office
Should not have
• No other logos or graphics outside of the logo provided.

```html
<!DOCTYPE html>
<html lang="en">
<head>
<meta charset="utf-8">
<title>Thistlewood Group Business Card</title>
<link rel="stylesheet" href="https://fonts.googleapis.com/css2?family=Arimo:wght@400;700&display=swap">
<style>
  :root {
    --ink: #1b1b1b;
    --ink-soft: #474747;
    --paper: #ffffff;
    --backdrop: #e4e4e4;
  }
  * { margin: 0; padding: 0; box-sizing: border-box; }
  html, body {
    width: 1200px;
    height: 667px;
    overflow: hidden;
    background: var(--backdrop);
    font-family: "Arimo", Arial, sans-serif;
  }
  .canvas {
    position: relative;
    width: 1200px;
    height: 667px;
  }
  .card {
    position: absolute;
    top: 196px;
    width: 480px;
    height: 274px;
    box-shadow: 0 10px 24px rgba(0, 0, 0, 0.12);
  }
  .card--front {
    left: 90px;
    background: var(--ink);
    display: flex;
    align-items: center;
    justify-content: center;
  }
  .card--back {
    left: 630px;
    background: var(--paper);
    color: var(--ink);
    display: flex;
    flex-direction: column;
    align-items: center;
    padding-top: 38px;
  }
  .brand {
    display: flex;
    align-items: center;
    gap: 12px;
  }
  .brand__dot {
    display: block;
    border-radius: 50%;
  }
  .brand--large .brand__dot {
    width: 26px;
    height: 26px;
    background: var(--paper);
  }
  .brand--large .brand__name {
    color: var(--paper);
    font-size: 34px;
    font-weight: 400;
    letter-spacing: 0.02em;
  }
  .brand--small .brand__dot {
    width: 14px;
    height: 14px;
    background: var(--ink);
  }
  .brand--small .brand__name {
    color: var(--ink);
    font-size: 16px;
    font-weight: 400;
    letter-spacing: 0.03em;
  }
  .person {
    margin-top: 16px;
    text-align: center;
  }
  .person__name {
    font-size: 25px;
    font-weight: 400;
    letter-spacing: 0.04em;
    color: var(--ink-soft);
    text-transform: uppercase;
  }
  .person__title {
    margin-top: 3px;
    font-size: 11px;
    font-weight: 700;
    color: var(--ink);
  }
  .contact {
    margin-top: 20px;
    list-style: none;
    text-align: center;
    font-size: 13px;
    line-height: 1.45;
    color: var(--ink-soft);
  }
</style>
</head>
<body>
  <main class="canvas">
    <section class="card card--front" aria-label="Card front">
      <div class="brand brand--large">
        <span class="brand__dot" aria-hidden="true"></span>
        <span class="brand__name">Thistlewood Group</span>
      </div>
    </section>

    <section class="card card--back" aria-label="Card back">
      <div class="brand brand--small">
        <span class="brand__dot" aria-hidden="true"></span>
        <span class="brand__name">Thistlewood Group</span>
      </div>
      <div class="person">
        <h1 class="person__name">Dana Whitfield</h1>
        <p class="person__title">Managing Director</p>
      </div>
      <ul class="contact">
        <li class="contact__phone">555.014.2276</li>
        <li class="contact__email">dwhitfield@thistlewoodgroup.com</li>
        <li class="contact__web">www.thistlewood.com</li>
      </ul>
    </section>
  </main>
</body>
</html>
```